Mail order Nursery needs banner for promoting perennials that compliment roses.

banner should be 1135 wide x165 tall. We have an existing one displayed but we are not happy with the way it is washed out. Use your creativity to give us something that pops. Would love to see some watercolor or some other form of image other than just words washed across a stock photo. Banner needs to read Perennial Companions for Roses or some variation of that. Colors need to compliment our current theme. You can view the page and banner I want to replace at www.meadowlarkbloomyard.com. The banner we want to replace has been uploaded to the pixel forum file drop box. Thanks for your help and I look forward to seeing what you guys come up with. EDIT: I don't think I was clear enough in by brief. This banner promotes the sale of plants that look good planted with roses. We are getting to many submissions that are using only roses as the backdrop. We are looking for different types of plants that you would grow in your garden to compliment your roses. Thanks for all your hard work.

Target Market(s)

Home owners between 30 and 65

Industry/Entity Type

Nursery

Colors
33a6d7
e667a6

Requirements
Must have
• Text promotion perennials that compliment roses.... does not have to be those exact words but get the point across
Should not have
• Stock Photos with simple text washed across it.

```html
<!DOCTYPE html>
<html lang="en">
<head>
<meta charset="utf-8">
<title>Perennial Companions for Roses – Banner</title>
<link rel="stylesheet" href="https://fonts.googleapis.com/css2?family=Cinzel:wght@400;600&display=swap">
<style>
  :root {
    --rose-pink: #e5177d;
    --leaf-green: #8dc63f;
    --olive-green: #7a8a2a;
    --crimson: #a3123e;
    --hot-pink: #ec2a7c;
    --blush: #f4a6c4;
    --white: #ffffff;
    --mist: #e6e6e6;
    --stone: #b9b9b9;
  }
  html, body {
    margin: 0;
    padding: 0;
    width: 1200px;
    height: 174px;
    overflow: hidden;
    background: var(--white);
  }
  .banner {
    display: block;
    width: 1200px;
    height: 174px;
  }
  .headline {
    font-family: "Cinzel", "Times New Roman", serif;
    font-weight: 600;
    fill: var(--rose-pink);
    stroke: var(--white);
    stroke-width: 5px;
    stroke-linejoin: round;
    paint-order: stroke fill;
    text-anchor: middle;
  }
</style>
</head>
<body>
<svg class="banner" viewBox="0 0 1135 165" width="1200" height="174" xmlns="http://www.w3.org/2000/svg" aria-labelledby="banner-title">
  <title id="banner-title">Perennial Companions for Roses</title>
  <defs>
    <linearGradient id="gardener-tones" x1="0" y1="0" x2="1" y2="0">
      <stop offset="0" stop-color="#e7a3bd"/>
      <stop offset="0.3" stop-color="#b87a86"/>
      <stop offset="0.55" stop-color="#9b9a3a"/>
      <stop offset="1" stop-color="#6f8a22"/>
    </linearGradient>
    <linearGradient id="shelf-tones" x1="0" y1="0" x2="1" y2="1">
      <stop offset="0" stop-color="#f2f2f2"/>
      <stop offset="0.5" stop-color="#d4d4d4"/>
      <stop offset="1" stop-color="#eeeeee"/>
    </linearGradient>
  </defs>

  <!-- potted plant shelves backdrop -->
  <rect class="plant-shelves" x="380" y="0" width="720" height="165" fill="url(#shelf-tones)" role="img" aria-label="Soft grey photo of potted perennials on white shelves"/>

  <!-- gardener with flowers -->
  <rect class="gardener-photo" x="0" y="0" width="400" height="165" fill="url(#gardener-tones)" role="img" aria-label="Photo of a gardener in a hat holding red flowers"/>

  <!-- left chevrons -->
  <polygon class="chevron-green" points="235,0 285,0 340,60 285,120 235,120 290,60" fill="var(--leaf-green)" opacity="0.9"/>
  <polygon class="chevron-white" points="330,0 378,0 460,82 378,165 330,165 412,82" fill="var(--white)"/>

  <!-- right chevron -->
  <polygon class="chevron-white-right" points="1000,0 1050,0 972,82 1050,165 1000,165 922,82" fill="var(--white)"/>

  <!-- right corner blocks -->
  <rect class="corner-backdrop" x="1050" y="0" width="85" height="165" fill="var(--blush)"/>
  <polygon class="corner-green" points="960,165 1050,75 1135,75 1135,165" fill="var(--leaf-green)"/>
  <polygon class="diamond-pink" points="1095,0 1135,0 1135,60 1105,85 1060,40" fill="var(--hot-pink)"/>
  <polygon class="diamond-crimson" points="1060,40 1105,85 1080,110 1035,65" fill="var(--crimson)" opacity="0.85"/>
  <polygon class="diamond-olive" points="1035,110 1080,65 1135,120 1135,165 1090,165" fill="var(--olive-green)" opacity="0.85"/>

  <!-- headline -->
  <text class="headline" x="680" y="80" font-size="36">Perennial Companions</text>
  <text class="headline" x="680" y="126" font-size="36">for Roses</text>
</svg>
</body>
</html>
```